Flyer Design for an electrical company

Hi i need a flyer designed for an electrical contracting company.
Company is based in Sydney, Australia.
We service the domestic market

This flyer will have general information about our services, our guarantees which are the important bit and a couple of offer boxes
E.g. save $97 complimentary electrical safety inspection, save $50 off your job, free power point replacement

Flyer to be two sided

size of flyer is DL, (210mm x 99mm)

Target Market(s)

Home owners

Industry/Entity Type

Electrical

Requirements
Must have
• Offer boxes save $97 complimentry electrical safety inspection,Save $50 off your job,free power point replacment, Save $150 OFF switchboard upgrades

Over $300 worth of savings!

heading: Your neighbourhood electrician

logo

www.wirebrightcrew.com.au
1300 584 672
my pic

Our promise to you...

1.We will arrive on time or we will pay you $100
2.Before any job begins you will know the exact cost
3.We will provide you with a fixed price guarantee assuring no extra costs
4.We will leave your place as clean as when we arrived
5.If there is a problem and it's our fault we will fix it for free
6.We will return your telephone calls promptly
7.We will provide a 12 Month warranty on all parts
8.We will provide friendly, helpful service and advice
..
Nice to have
• on the back of flyer: testimonials..

Here is what some of my customers have had to say...
Very satisfied...
“I am a very satisfied customer!!
Gordon promptly returned by initial email, was very professional in all of his communications
(even ringing me advising me he was going to be running a little late)
Gordon did a fantastic job installing 3 ceiling fans and was very tidy in the process. I have no
hesitation in hiring Gordon in the future, and recommending him to family and friends”.
Rosalind Pemberwick - North Strathfield
Removed all the stress...
What a breath of fresh air...

“Thanks Gordon!
You managed to sort out our electrical problem- this was a problem that another electrician
couldn't resolve after two attempts and a problem which many other electricians shide away
from (messages were left but no one no returned my call).
After eight weeks of stress I contacted Gordon, what a breath of fresh air! Not only did he
give helpful advice over the phone but he was out promptly (and on time) to assess the
problem and provide a written quote. Gordon even contacted us the day before to confirm
the job and was then here on time to start work.
The job was completed in a professional and friendly manner and we haven't had a problem
since.
To top it off Gordon also replaced numerous power points which we had purchased but not
yet installed- all without additional charge. He was clean and tidy- what more could you ask
for. I highly recommend Gordon services whose details I have already given to family and
friends. Thanks Gordon”
Trevor, Helen & Molly - Narwee

Extremely professional...
“Gordon was extremely professional. He arrived when he said he would, quoted the job,
came back with a written quote and was very reasonable. He also checked out our smoke
detectors whist he was here. He installed 2 ceiling fans and an outdoor power point. He
cleaned up the mess and was very efficient. I will definitely use him again and recommend
him to friends”
Yvonne Harker - Croydon

```html
<!DOCTYPE html>
<html lang="en">
<head>
<meta charset="utf-8">
<title>Your Neighbourhood Electrician – Wirebright Crew</title>
<link rel="stylesheet" href="https://fonts.googleapis.com/css2?family=Anton&family=Oswald:wght@600;700&family=Archivo:wght@800&family=Roboto:wght@400;700&display=swap">
<style>
  :root {
    --page: #ffffff;
    --navy-deep: #0b1f4a;
    --navy: #1a2f7a;
    --blue-glow: #3f8fd0;
    --teal-glow: #8fd2e6;
    --headline-red: #d0102a;
    --orange: #ef7d0a;
    --white: #ffffff;
    --band: #ffffff;
    --edge: #c9cdd3;
    --card-grey: #d9dde3;
    --shirt-blue: #2a56b8;
  }
  * { margin: 0; padding: 0; box-sizing: border-box; }
  html, body { width: 1200px; height: 650px; overflow: hidden; background: var(--page); }
  .canvas { position: relative; width: 1200px; height: 650px; }

  .flyer {
    position: absolute; left: 76px; top: 79px; width: 1048px; height: 490px;
    overflow: hidden;
    border: 1px solid var(--edge);
    background:
      radial-gradient(ellipse 420px 260px at 760px 230px, var(--teal-glow) 0%, rgba(143,210,230,0.35) 40%, rgba(63,143,208,0) 75%),
      radial-gradient(ellipse 500px 300px at 300px 250px, rgba(63,143,208,0.55) 0%, rgba(63,143,208,0) 70%),
      linear-gradient(160deg, var(--navy-deep) 0%, #173a7c 55%, #0d2356 100%);
    font-family: "Oswald", "Arial Narrow", sans-serif;
  }

  .site-url {
    position: absolute; left: 55px; top: 14px;
    font-family: "Roboto", Arial, sans-serif; font-weight: 700; font-size: 19px; line-height: 1;
    color: var(--white); letter-spacing: 0.3px;
  }
  .headline {
    position: absolute; left: 24px; top: 42px;
    font-family: "Anton", Impact, sans-serif; font-weight: 400; font-size: 66px; line-height: 1.1;
    color: var(--headline-red);
    letter-spacing: -0.5px;
    text-shadow:
      2px 0 0 var(--white), -2px 0 0 var(--white), 0 2px 0 var(--white), 0 -2px 0 var(--white),
      2px 2px 0 var(--white), -2px -2px 0 var(--white), 2px -2px 0 var(--white), -2px 2px 0 var(--white),
      3px 5px 5px rgba(0,0,0,0.45);
  }

  .licence {
    position: absolute; left: 16px; top: 398px; transform: rotate(-90deg); transform-origin: left top;
    font-family: "Roboto", Arial, sans-serif; font-size: 10px; line-height: 1; color: var(--white); white-space: nowrap;
  }

  .savings-total {
    position: absolute; right: 806px; top: 138px; text-align: right;
    color: var(--white); font-family: "Anton", Impact, sans-serif; line-height: 1.02;
    text-shadow: 1px 2px 3px rgba(0,0,0,0.35);
  }
  .savings-total .over { font-size: 56px; display: block; }
  .savings-total .amount { font-size: 90px; display: block; line-height: 0.95; }
  .savings-total .worth { font-size: 52px; display: block; }
  .savings-total .word { font-size: 52px; display: block; }

  .pointer { position: absolute; left: 258px; top: 147px; }

  .offer {
    position: absolute; border-radius: 18px; overflow: hidden; text-align: center;
    box-shadow: 2px 4px 8px rgba(0,0,0,0.35);
  }
  .offer .lead { background: var(--white); color: var(--orange); font-weight: 700; line-height: 1; }
  .offer .detail { background: var(--orange); color: var(--white); font-weight: 700; line-height: 1.2; }

  .offer-inspection { left: 309px; top: 131px; width: 218px; height: 177px; transform: rotate(-1.5deg); }
  .offer-inspection .lead { font-size: 42px; padding: 8px 0 6px; }
  .offer-inspection .detail { font-size: 21px; height: 100%; padding-top: 8px; }

  .offer-powerpoint { left: 559px; top: 124px; width: 165px; height: 108px; transform: rotate(-1deg); }
  .offer-powerpoint .lead { font-size: 30px; padding: 4px 0 2px; }
  .offer-powerpoint .detail { font-size: 15px; height: 100%; padding-top: 8px; }

  .offer-job { left: 343px; top: 322px; width: 159px; height: 83px; transform: rotate(1deg); }
  .offer-job .lead { font-size: 32px; padding: 6px 0 4px; }
  .offer-job .detail { font-size: 15px; height: 100%; padding-top: 5px; }

  .offer-switchboard { left: 544px; top: 245px; width: 222px; height: 156px; transform: rotate(-1deg); }
  .offer-switchboard .lead { font-size: 42px; padding: 8px 0 6px; }
  .offer-switchboard .detail { font-size: 22px; height: 100%; padding-top: 10px; }

  .portrait {
    position: absolute; left: 768px; top: 0; width: 280px; height: 490px;
    background: linear-gradient(180deg, rgba(180,225,240,0.0) 0%, rgba(90,120,190,0.35) 40%, var(--shirt-blue) 75%, #1d3f93 100%);
  }

  .contact-band {
    position: absolute; left: 0; bottom: 0; width: 768px; height: 72px; background: var(--band);
  }
  .call-label {
    position: absolute; left: 24px; top: 14px;
    font-family: "Oswald", "Arial Narrow", sans-serif; font-weight: 700; font-size: 34px; line-height: 1.2; color: var(--navy);
  }
  .phone {
    position: absolute; left: 154px; top: 6px;
    font-family: "Archivo", "Arial Black", sans-serif; font-weight: 800; font-size: 52px; line-height: 1.1; color: var(--navy); letter-spacing: 2px;
  }
  .payment-cards { position: absolute; left: 559px; top: 17px; display: flex; gap: 8px; }
  .payment-cards span { display: block; width: 62px; height: 38px; border: 2px solid var(--card-grey); border-radius: 3px; background: #f2f4f7; }

  .brand-mark {
    position: absolute; left: 786px; top: 382px; width: 200px;
    font-family: "Anton", Impact, sans-serif; font-size: 26px; line-height: 1.05;
    color: var(--orange);
    display: flex; align-items: center; gap: 8px;
  }
  .brand-mark .dot { flex: none; width: 14px; height: 14px; border-radius: 50%; background: var(--orange); }
</style>
</head>
<body>
<div class="canvas">
  <section class="flyer">
    <div class="portrait" role="img" aria-label="Photo of the electrician smiling, arms crossed, holding a light bulb"></div>

    <p class="site-url">www.wirebrightcrew.com.au</p>
    <h1 class="headline">Your Neighbourhood Electrician</h1>

    <p class="licence">Lic: 318492C | ABN: 27590314865</p>

    <p class="savings-total">
      <span class="over">Over</span>
      <span class="amount">$300</span>
      <span class="worth">worth of</span>
      <span class="word">savings!</span>
    </p>

    <svg class="pointer" width="44" height="254" viewBox="0 0 44 254" aria-hidden="true">
      <polygon points="0,0 44,127 0,254" fill="#ffffff"/>
    </svg>

    <div class="offer offer-inspection">
      <p class="lead">Save $97</p>
      <p class="detail">complimentary<br>electrical safety<br>inspection</p>
    </div>

    <div class="offer offer-powerpoint">
      <p class="lead">Free</p>
      <p class="detail">power point<br>replacement</p>
    </div>

    <div class="offer offer-job">
      <p class="lead">Save $50</p>
      <p class="detail">OFF your job</p>
    </div>

    <div class="offer offer-switchboard">
      <p class="lead">Save $150</p>
      <p class="detail">OFF switchboard<br>upgrades</p>
    </div>

    <div class="contact-band">
      <p class="call-label">CALL US</p>
      <p class="phone">1300 584 672</p>
      <div class="payment-cards" aria-label="Accepted payment cards">
        <span></span><span></span><span></span>
      </div>
    </div>

    <p class="brand-mark"><span class="dot"></span><span>Wirebright Crew<br>Pty Ltd</span></p>
  </section>
</div>
</body>
</html>
```